Flyer-Design für psychologisches Coaching  und Taiji
Flyer-Design für psychologisches Coaching und Taiji
Zielgruppe
Seit Januar 2020 habe ich mich selbständig gemacht und biete unter dem Namen 'WANDELRAUM - Mara Brenner, Coaching und Bewegung' Coaching sowie Taiji an. Der Corona-Lockdown hat meinen Geschäftseintritt stark beeinflusst, so dass ich für den Restart einen professionellen Flyer benötige, um mich und mein Angebot bekannt zu machen. Die Flyer werde ich vor meinen Räumen sowie in Geschäften im Umkreis und/oder per Einwurf verteilen.
Meine Zielgruppe sind gesundheitsorientierte Menschen in der zweiten Lebenshälfte, die ihre Balance finden wollen.
Mehr im separaten Dokument, bitte lesen.
Aufgabenstellung
Das Design soll zum Logo und zu meinem angestrebten Image passen. Ich möchte seriös, sympathisch und authentisch rüberkommen. Das psychologische Coaching und Taiji sollen gleichwertig und harmonisch präsentiert werden. Die Texte sollen kurz und prägnant sein. Textvorschläge gebe ich im Briefing und freue mich über neue, aussagefähige Formulierungen.
Mehr im beigefügten Dokument, bitte lesen.

```html
<!DOCTYPE html>
<html lang="de">
<head>
<meta charset="utf-8">
<title>Aktuelle Termine Wandelraum – Sommer 2020</title>
<link href="https://fonts.googleapis.com/css2?family=Carlito:wght@400;700&family=Open+Sans:wght@600;700&display=swap" rel="stylesheet">
<style>
  :root{
    --olive:#a39c3c;
    --olive-text:#a19a35;
    --sage:#d5d3a6;
    --ink:#1a1a1a;
    --paper:#ffffff;
    --page:#ffffff;
  }
  *{margin:0;padding:0;box-sizing:border-box}
  html,body{width:1200px;height:848px;overflow:hidden;background:var(--page)}
  .canvas{position:relative;width:1200px;height:848px;overflow:hidden}
  .flyer{position:absolute;left:407px;top:0;width:401px;height:848px;background:var(--paper);overflow:hidden;font-family:"Carlito","Calibri",sans-serif;color:var(--ink)}
  .header-band{position:absolute;left:0;top:0;width:401px;height:172px}
  .header-title{position:absolute;left:37px;top:33px;font-family:"Open Sans",sans-serif;font-weight:700;color:#fff;font-size:26.5px;line-height:30px;letter-spacing:1.2px}
  .figure-area{position:absolute;left:249px;top:398px;width:152px;height:372px;background:linear-gradient(180deg,#dad8b0 0%,var(--sage) 60%);border-radius:70px 0 0 0}
  .section-title{position:absolute;left:37px;color:var(--olive-text);font-weight:700;font-size:15.6px;line-height:21px}
  .trial-title{top:193px}
  .meditation-title{top:634px}
  .body-text{position:absolute;left:37px;font-size:13.4px;line-height:17.4px}
  .intro{top:244px}
  .notes{top:323px}
  .dates{position:absolute;left:37px;border-collapse:collapse;font-size:13.4px}
  .dates td{height:20.7px;padding:0;vertical-align:middle}
  .dates tr+tr td{border-top:1.3px solid var(--olive)}
  .dates .day{width:36px;text-align:center;border-right:1.3px solid var(--olive)}
  .dates .slot{width:157px;padding-left:6px}
  .trial-dates{top:425px}
  .meditation-dates{top:683px}
  .footer-band{position:absolute;left:0;top:748px;width:401px;height:100px}
  .footer{position:absolute;left:0;top:796px;width:401px;text-align:center;color:#fff;font-family:"Carlito",sans-serif;font-size:10.4px;line-height:14.3px}
  .footer strong{font-weight:700}
</style>
</head>
<body>
<div class="canvas">
  <div class="flyer">
    <svg class="header-band" viewBox="0 0 401 172" aria-hidden="true">
      <path d="M0 0H401V134C300 140 180 148 0 150Z" fill="var(--olive)"/>
      <path d="M0 150C150 152 280 144 401 134V150C300 158 180 168 0 164Z" fill="var(--sage)"/>
      <path d="M0 158C140 162 270 156 401 146" stroke="#fff" stroke-width="1.5" fill="none" opacity=".8"/>
      <path d="M0 166C140 172 260 166 401 154" stroke="var(--sage)" stroke-width="2" fill="none"/>
    </svg>
    <h1 class="header-title">AKTUELLE TERMINE<br>WANDELRAUM IM<br>SOMMER 2020</h1>

    <div class="figure-area" role="img" aria-label="Silhouette einer Person in Taiji-Bewegung mit erhobenem Arm"></div>

    <h2 class="section-title trial-title">Kostenlose Schnupperstunde Taiji,<br>Qigong und Meditation</h2>
    <p class="body-text intro">Eine Schnupperstunde dauert 75 min und beinhaltet<br>einen Mix aus Taiji, Qigong und Meditation. So können<br>Sie es zuerst ausprobieren, bevor Sie in einen laufenden<br>Kurs einsteigen.</p>
    <p class="body-text notes">Bitte seien sie mindestens 10 min vor Beginn der<br>Stunde da, um sich entsprechend einstimmen zu<br>können. Tragen Sie bequeme Sportkleidung und<br>warme Socken oder Taiji-Schuhe. Auch Stoppersocken<br>oder Barfußschuhe sind okay.</p>

    <table class="dates trial-dates">
      <tr><td class="day">MI</td><td class="slot">01.07. - 18:30-19:45 Uhr</td></tr>
      <tr><td class="day">MI</td><td class="slot">08.07. - 18:30-19:45 Uhr</td></tr>
      <tr><td class="day">DO</td><td class="slot">16.07. - 19:45-21:00 Uhr</td></tr>
      <tr><td class="day">MO</td><td class="slot">20.07. - 20:00-21:15 Uhr</td></tr>
      <tr><td class="day">MI</td><td class="slot">29.07. - 19:00-20:15 Uhr</td></tr>
      <tr><td class="day">DO</td><td class="slot">06.08. - 19:30-20:45 Uhr</td></tr>
      <tr><td class="day">MO</td><td class="slot">10.08. - 20:00-21:15 Uhr</td></tr>
      <tr><td class="day">MI</td><td class="slot">19.08. - 19:00-20:15 Uhr</td></tr>
      <tr><td class="day">FR</td><td class="slot">28.08. - 19:00-20:15 Uhr</td></tr>
    </table>

    <h2 class="section-title meditation-title">Nächste offene<br>Meditationsabende:</h2>
    <table class="dates meditation-dates">
      <tr><td class="day">FR</td><td class="slot">24.07. - 19:00-20:15 Uhr</td></tr>
      <tr><td class="day">MI</td><td class="slot">26.08. - 19:30-20:45 Uhr</td></tr>
    </table>

    <svg class="footer-band" viewBox="0 0 401 100" aria-hidden="true">
      <path d="M0 12C140 20 280 14 401 2V100H0Z" fill="var(--olive)"/>
      <path d="M0 14C130 18 260 14 401 6" stroke="#fff" stroke-width="2.5" fill="none"/>
      <path d="M20 21C150 24 270 18 380 12" stroke="#fff" stroke-width="1.6" fill="none" opacity=".85"/>
    </svg>
    <div class="footer">
      <strong>Wandelraum – Mara Brenner Coaching und Bewegung</strong><br>
      Lindenweg 12 • 61350 Talheim<br>
      www.wandelraum-coaching.de • info@wandelraum-coaching.de • <strong>0151 234 56 78</strong>
    </div>
  </div>
</div>
</body>
</html>
```